Wellspring Renewal Collective Botswana Africa Flyer

Create an A5 double sided flyer to advertise a campus lifestyle wellness training at the university of Tselakgang. This flyer invite all interested to freely attend naturopathic treatment training, stop addiction training, music therapy training lessons. Conducted by Wellspring Renewal Collective. The lead facilitator is Marisol-Ann Okoye.
Flyer text available at 'must haves'

Target Market(s)

University students

Industry/Entity Type

Training

Requirements
Must have
• Logo (supplied)
• Picture of Marisol-Ann Okoye, our Lead Facilitator (supplied)
• Music pic. Classical hym choir or preferably orchestra of predominantly black youth
• And the text must be as follows:
• WELLSPRING RENEWAL COLLECTIVE (WRC) is a non profit organization that conducts wholistic health programs in Universities aimed at reversing Lifestyle Diseases and breaking down the chains of Drug Addiction and Satanism among the youth. We conduct a 3 hour practical training every week on disease treatment protocols, stop addiction and music therapy.
• 1. Disease Treatment Programs: We thoroughly train you to use food, herbs, natural remedies and scientifically proven lifestyle changes to reverse lifestyle diseases such as diabetes, arthritis, cancer and hypertension.
• 2. Stop Addiction Programs: We also teach you how to administer a 10 day treatment protocol to wipe out the craving for drugs such cocaine, marijuana and tobacco, and to also rehabilitate those freed from these addictions.
• 3. Music Therapy: Top notch musical training will equip you to efficiently administer music therapy to heal the soul and relief tensions in any community using voice and musical instruments. Music, when properly done, heals both the singer and the one to whom it is sung!
• These training protocols will not only help you but most importantly will equip you to effectively help others!
• THE MUSIC CONNECTION
• Music is part of our being. There is a kind of music that goes to the waist igniting in us the desire for illicit sex, drugs and all recklessness. And there is a type of music that touches the heart and bring us closer to our Maker, igniting feelings of sympathy, kindness and generosity to our fellow man.
• When we are happy, a song always says it best. When we are sad, music has a way of saying it in ways that words would never reach. And when there is a call to action, a cause to which the sleeping needs to be awakened, music makes a perfect wake up call!
• The cause of WRC is a liberation struggle that cannot do without music. For when the chains of addiction are broken down, the joy that comes cannot be expressed in talking tones. And since it was through music that our captivity was perpetuated, it's only befitting that our liberation must be sustained through song. It is a new song though, which we shall first learn to sing in voice, and then through musical instruments of harps, violins and keyboards. A Quadrangle Ensemble of Daybreak, singing Meadowlight Hymns! You ought to be a part of it!
• THIS VALUABLE TRAINING THAT IS WORTH LOTS OF MONEY ELSEWHERE IS NOW BROUGHT TO YOU FREE OF CHARGE. TO ENROLL IMMEDIATELY CALL 71450362 or EMAIL: WRC2016@kelvora.com

```html
<!DOCTYPE html>
<html lang="en">
<head>
<meta charset="utf-8">
<title>Wellspring Renewal Collective – Campus Wellness Training Flyer</title>
<link rel="stylesheet" href="https://fonts.googleapis.com/css2?family=Open+Sans:wght@400;600;700;800&display=swap">
<style>
  :root {
    --green: #149a2a;
    --green-dark: #0e7f21;
    --red: #d9252b;
    --ink: #1f1f1f;
    --paper: #ffffff;
    --backdrop: #d8d8d5;
    --caption-grey: #d4d4d4;
  }
  * { box-sizing: border-box; margin: 0; padding: 0; }
  html, body { width: 1200px; height: 900px; overflow: hidden; }
  body {
    background: var(--backdrop);
    font-family: "Open Sans", Arial, sans-serif;
    color: var(--ink);
  }
  .stage { position: relative; width: 1200px; height: 900px; }
  .flyer-side {
    position: absolute;
    top: 39px;
    width: 524px;
    height: 731px;
    background: var(--paper);
    box-shadow: 0 4px 14px rgba(0,0,0,.25);
    overflow: hidden;
  }
  .flyer-side--front { left: 59px; }
  .flyer-side--back { left: 621px; }

  /* brand block */
  .brand {
    display: flex; flex-direction: column; align-items: center; gap: 6px;
    text-align: center;
  }
  .brand__dot { width: 58px; height: 58px; border-radius: 50%; background: var(--red); }
  .brand__name {
    font-size: 10.5px; font-weight: 800; color: var(--green); letter-spacing: .2px;
    line-height: 1.15;
  }

  /* front side */
  .hero-photo {
    position: absolute; left: 0; top: 0; width: 524px; height: 318px;
    background:
      radial-gradient(circle at 40% 45%, #3c5f9a 0%, transparent 45%),
      radial-gradient(circle at 85% 70%, #b0397a 0%, transparent 40%),
      linear-gradient(120deg, #1b7d6e 0%, #203a6e 40%, #4a2a6c 75%, #2a1a3e 100%);
  }
  .hero-brand {
    position: absolute; right: 22px; top: 24px; width: 176px; height: 112px;
    background: var(--paper); border-radius: 10px; padding-top: 10px;
  }
  .corner-dot {
    position: absolute; width: 30px; height: 30px; border-radius: 50%;
    background: var(--green);
  }
  .front-dot { left: -15px; top: 305px; }
  .front-body { position: absolute; left: 28px; right: 24px; top: 326px; }
  .intro { font-size: 12.6px; line-height: 1.3; text-align: justify; }
  .intro strong { color: var(--green); font-weight: 800; }
  .program { position: relative; padding-left: 44px; margin-top: 14px; }
  .program--music { padding-left: 66px; }
  .program__icon {
    position: absolute; left: -8px; top: 2px; width: 40px; height: 40px; border-radius: 50%;
    background: var(--red);
  }
  .program--music .program__icon { background: var(--green); width: 58px; height: 48px; border-radius: 50%; }
  .program__title { font-size: 13px; font-weight: 800; color: var(--red); line-height: 1.2; }
  .program--music .program__title { color: var(--green); }
  .program__text { font-size: 12.3px; line-height: 1.28; text-align: justify; }
  .front-closing {
    position: absolute; left: 40px; right: 40px; top: 659px;
    font-size: 10.6px; font-weight: 800; text-align: center; line-height: 1.25;
  }
  .contact-bar {
    position: absolute; left: 0; right: 0; top: 689px; height: 34px;
    background: var(--green); color: var(--paper);
    display: flex; align-items: center; justify-content: center;
    font-size: 15px;
  }

  /* back side */
  .back-dot { left: -15px; top: 14px; }
  .music-copy { position: absolute; left: 28px; top: 22px; width: 318px; }
  .music-copy__title { font-size: 14.5px; font-weight: 800; color: var(--green); margin-bottom: 3px; }
  .music-copy p { font-size: 12.2px; line-height: 1.29; text-align: justify; margin-bottom: 7px; }
  .music-copy p + p { text-indent: 14px; }
  .back-brand { position: absolute; left: 354px; top: 34px; width: 158px; }
  .facilitator-photo {
    position: absolute; left: 354px; top: 143px; width: 154px; height: 198px;
    background: linear-gradient(180deg, #d9d4cc 0%, #b79c86 55%, #e9e6e2 100%);
  }
  .facilitator-caption {
    position: absolute; left: 354px; top: 341px; width: 154px; height: 40px;
    background: var(--caption-grey); text-align: center; padding-top: 4px;
  }
  .facilitator-caption__name { font-size: 11px; font-weight: 800; }
  .facilitator-caption__role { font-size: 11px; }
  .ensemble-call {
    position: absolute; left: 10px; right: 10px; top: 399px;
    font-size: 11.4px; font-weight: 800; text-align: center; line-height: 1.25;
  }
  .ensemble-photo {
    position: absolute; left: 0; top: 433px; width: 524px; height: 150px;
    background: linear-gradient(90deg, #2a1a16 0%, #7a2434 25%, #c2305a 45%, #6a3a2c 70%, #1d1512 100%);
  }
  .offer-panel {
    position: absolute; left: 0; right: 0; top: 583px; height: 140px;
    background: var(--green); color: var(--paper); text-align: center;
    padding-top: 12px;
  }
  .offer-panel__lead { font-size: 15px; line-height: 1.3; letter-spacing: .1px; }
  .offer-panel__cta { font-size: 22px; margin-top: 8px; letter-spacing: .3px; }
  .offer-panel__contact { font-size: 21px; font-weight: 700; margin-top: 4px; }
  .offer-panel__contact span { font-weight: 400; font-size: 17px; }
</style>
</head>
<body>
<main class="stage">

  <section class="flyer-side flyer-side--front">
    <div class="hero-photo" role="img" aria-label="Young choir singers performing on a colourfully lit stage"></div>
    <div class="hero-brand brand">
      <span class="brand__dot"></span>
      <span class="brand__name">WELLSPRING RENEWAL COLLECTIVE</span>
    </div>
    <span class="corner-dot front-dot"></span>

    <div class="front-body">
      <p class="intro"><strong>WELLSPRING RENEWAL COLLECTIVE (WRC)</strong> is a non profit organization that conducts wholistic health programs in Universities aimed at reversing Lifestyle Diseases and breaking down the chains of Drug Addiction and Satanism among the youth. We conduct a 3 hour practical training every week on disease treatment protocols, stop addiction and music therapy.</p>

      <div class="program">
        <span class="program__icon"></span>
        <h2 class="program__title">DISEASE TREATMENT PROGRAMS</h2>
        <p class="program__text">We thoroughly train you to use food, herbs, natural remedies and scientifically proven lifestyle changes to reverse lifestyle diseases such as diabetes, arthritis, cancer and hypertension.</p>
      </div>

      <div class="program">
        <span class="program__icon"></span>
        <h2 class="program__title">STOP ADDICTION PROGRAMS</h2>
        <p class="program__text">We also teach you how to administer a 10 day treatment protocol to wipe out the craving for drugs such cocaine, marijuana and tobacco, and to also rehabilitate those freed from these addictions.</p>
      </div>

      <div class="program program--music">
        <span class="program__icon"></span>
        <h2 class="program__title">MUSIC THERAPY</h2>
        <p class="program__text">Top notch musical training will equip you to efficiently administer music therapy to heal the soul and relief tensions in any community using voice and musical instruments. Music, when properly done, heals both the singer and the one to whom it is sung!</p>
      </div>
    </div>

    <p class="front-closing">THESE TRAINING PROTOCOLS WILL NOT ONLY HELP YOU BUT MOST IMPORTANTLY WILL EQUIP YOU TO EFFECTIVELY HELP OTHERS!</p>
    <div class="contact-bar">71450362 or email: WRC2016@kelvora.com</div>
  </section>

  <section class="flyer-side flyer-side--back">
    <span class="corner-dot back-dot"></span>
    <article class="music-copy">
      <h2 class="music-copy__title">THE MUSIC CONNECTION</h2>
      <p>Music is part of our being. There is a kind of music that goes to the waist igniting in us the desire for illicit sex, drugs and all recklessness. And there is a type of music that touches the heart and bring us closer to our Maker, igniting feelings of sympathy, kindness and generosity to our fellow man.</p>
      <p>When we are happy, a song always says it best. When we are sad, music has a way of saying it in ways that words would never reach. And when there is a call to action, a cause to which the sleeping needs to be awakened, music makes a perfect wake up call!</p>
      <p>The cause of WRC is a liberation struggle that cannot do without music. For when the chains of addiction are broken down, the joy that comes cannot be expressed in talking tones. And since it was through music that our captivity was perpetuated, it's only befitting that our liberation must be sustained through song. It is a new song though, which we shall first learn to sing in voice, and then through musical instruments of harps, violins and keyboards.</p>
    </article>

    <div class="back-brand brand">
      <span class="brand__dot"></span>
      <span class="brand__name">WELLSPRING RENEWAL COLLECTIVE</span>
    </div>
    <div class="facilitator-photo" role="img" aria-label="Portrait of Marisol-Ann Okoye, Lead Facilitator"></div>
    <div class="facilitator-caption">
      <p class="facilitator-caption__name">MARISOL-ANN OKOYE</p>
      <p class="facilitator-caption__role">Lead Facilitator</p>
    </div>

    <p class="ensemble-call">A QUADRANGLE ENSEMBLE OF DAYBREAK, SINGING MEADOWLIGHT HYMNS!<br>YOU OUGHT TO BE A PART OF IT!</p>
    <div class="ensemble-photo" role="img" aria-label="Youth choir in red and white robes singing on stage"></div>

    <div class="offer-panel">
      <p class="offer-panel__lead">THIS VALUABLE TRAINING THAT IS WORTH LOTS OF MONEY<br>ELSEWHERE IS NOW BROUGHT TO YOU FREE OF CHARGE.</p>
      <p class="offer-panel__cta">TO ENROLL IMMEDIATELY CALL</p>
      <p class="offer-panel__contact">71450362 <span>or email:</span> WRC2016@kelvora.com</p>
    </div>
  </section>

</main>
</body>
</html>
```